#SkyLanternYo - One man's journey to becoming a corporate escapee and how you can do it too!

A book that describes my journey from avoiding spy allegations in Abu Dhabi, drinking vodka with Senators in Moscow, avoiding TVR and Mafia in Uzbekistan, being shot at in Jakarta, evacuated out of riots in Ranchi India and evading custody in Beijing. It is how the importance of life was realised and the opportunity break out and disrupt the boring old politically driven large corporates by developing new platforms on the internet to provide better and cheaper new products and services.

```html
<!DOCTYPE html>
<html lang="en">
<head>
<meta charset="utf-8">
<title>#SkyLantern Yo – Book Cover</title>
<link rel="stylesheet" href="https://fonts.googleapis.com/css2?family=Oswald:wght@500;700&family=Didact+Gothic&family=Questrial&display=swap">
<style>
  :root {
    --canvas-bg: #e9e9e9;
    --cover-white: #fbfbfb;
    --back-grey: #ececec;
    --accent-orange: #e2551b;
    --ink-black: #141414;
    --text-dark: #2b2b2b;
    --box-black: #0d0d0d;
    --box-label: #6b6b6b;
    --photo-dark: #2c2c2e;
    --photo-light: #f4f4f4;
    --photo-orange: #e8683c;
  }
  * { margin: 0; padding: 0; box-sizing: border-box; }
  html, body {
    width: 1200px; height: 800px; overflow: hidden;
    background: var(--canvas-bg);
  }
  .canvas {
    position: relative; width: 1200px; height: 800px;
  }
  .cover {
    position: absolute; top: 90px; width: 400px; height: 620px;
    box-shadow: 0 6px 18px rgba(0,0,0,0.12);
  }

  /* Back cover */
  .back-cover {
    left: 150px; background: var(--back-grey);
    padding: 22px 28px 0 28px;
  }
  .back-cover__author {
    text-align: right;
    font-family: 'Oswald', sans-serif; font-weight: 700;
    font-size: 16px; color: var(--ink-black);
  }
  .back-cover__title {
    margin-top: 2px;
    font-family: 'Oswald', sans-serif; font-weight: 500;
    font-size: 46px; line-height: 1.05; color: var(--accent-orange);
    letter-spacing: -0.5px;
  }
  .back-cover__subtitle {
    margin-top: 10px; text-align: center;
    font-family: 'Questrial', sans-serif; font-weight: 700;
    font-size: 13.5px; line-height: 1.3; color: var(--ink-black);
  }
  .back-cover__blurb {
    margin-top: 22px;
    font-family: 'Didact Gothic', sans-serif;
    font-size: 12.6px; line-height: 1.22; color: var(--text-dark);
    text-align: justify;
  }
  .back-cover__slots {
    position: absolute; left: 28px; right: 28px; bottom: 28px;
    display: flex; justify-content: space-between;
  }
  .slot {
    width: 124px; height: 72px; background: var(--box-black);
    display: flex; align-items: center; justify-content: center;
    font-family: 'Didact Gothic', sans-serif; font-size: 11px;
    color: var(--box-label); letter-spacing: 0.5px;
  }

  /* Front cover */
  .front-cover {
    left: 650px; background: var(--cover-white);
  }
  .front-cover__photo {
    display: block; width: 400px; height: 380px;
  }
  .front-cover__title {
    margin: 28px 0 0 22px;
    font-family: 'Oswald', sans-serif; font-weight: 500;
    font-size: 52px; line-height: 1; color: var(--accent-orange);
    letter-spacing: -0.5px;
  }
  .front-cover__subtitle {
    margin: 12px 0 0 22px;
    font-family: 'Questrial', sans-serif;
    font-size: 15.5px; line-height: 1.25; color: var(--ink-black);
  }
  .highlight {
    color: var(--accent-orange); font-weight: 700;
  }
  .front-cover__author {
    margin-top: 22px; text-align: center;
    font-family: 'Oswald', sans-serif; font-weight: 700;
    font-size: 28px; color: var(--ink-black);
  }
</style>
</head>
<body>
<main class="canvas">

  <section class="cover back-cover">
    <p class="back-cover__author">Martin K. Hale</p>
    <h2 class="back-cover__title">#SkyLantern Yo</h2>
    <p class="back-cover__subtitle">One man's journey to becoming <span class="highlight">a corporate escapee</span><br>and <span class="highlight">how you can do it too!</span></p>
    <p class="back-cover__blurb">Lorem ipsum dolor sit amet, consectetur adipisicing elit, sed do eiusmod tempor incididunt ut labore et dolore magna aliqua. Ut enim ad minim veniam, quis nostrud exercitation. Lorem ipsum dolor sit amet, consectetur adipisicing elit, sed do eiusmod tempor incididunt ut labore et dolore magna aliqua. Ut enim ad minim veniam, quis nostrud exercitation. Lorem ipsum dolor sit amet, consectetur adipisicing elit, sed do eiusmod tempor incididunt ut labore et dolore magna aliqua. Ut enim ad minim veniam, quis nostrud exercitation. Lorem ipsum dolor sit amet, consectetur adipisicing elit, sed do eiusmod tempor incididunt ut labore et dolore magna aliqua. Ut enim ad minim veniam, quis nostrud exercitation. Lorem ipsum dolor sit amet, consectetur adipisicing elit, sed do eiusmod tempor incididunt ut labore et dolore magna aliqua. Ut enim ad minim veniam, quis nostrud exercitation. Lorem ipsum dolor sit amet, consectetur adipisicing elit, sed do eiusmod tempor incididunt ut labore et dolore magna aliqua. Ut enim ad minim veniam, quis nostrud exercitation. Lorem ipsum dolor sit amet, consectetur adipisicing elit, sed do eiusmod tempor incididunt.</p>
    <div class="back-cover__slots">
      <div class="slot">LOGO</div>
      <div class="slot">ISBN</div>
    </div>
  </section>

  <section class="cover front-cover">
    <svg class="front-cover__photo" viewBox="0 0 400 380" role="img" aria-label="Photo of two men seen from the waist down: one in a black business suit and shoes, the other in orange patterned shorts and orange sneakers">
      <defs>
        <linearGradient id="photoTones" x1="0" y1="0" x2="1" y2="0">
          <stop offset="0" stop-color="var(--photo-light)"/>
          <stop offset="0.3" stop-color="var(--photo-dark)"/>
          <stop offset="0.5" stop-color="var(--photo-light)"/>
          <stop offset="0.75" stop-color="var(--photo-orange)"/>
          <stop offset="1" stop-color="var(--photo-light)"/>
        </linearGradient>
      </defs>
      <rect width="400" height="380" fill="url(#photoTones)"/>
    </svg>
    <h1 class="front-cover__title">#SkyLantern Yo</h1>
    <p class="front-cover__subtitle">One man's journey to becoming <span class="highlight">a corporate escapee</span><br>and <span class="highlight">how you can do it too!</span></p>
    <p class="front-cover__author">Martin K. Hale</p>
  </section>

</main>
</body>
</html>
```